We need a web page design for a new company called "Quarry". We provide an innovative music sharing mobile application that allows music listeners to share their music without paying for a monthly subscription. We would like to incorporate the attached logo and color scheme. The final design should communicate music gifting and sharing.

Industry/Entity Type

It Company

```html
<!DOCTYPE html>
<html lang="en">
<head>
<meta charset="utf-8">
<title>Quarry — Share Your Songs</title>
<link href="https://fonts.googleapis.com/css2?family=Open+Sans:ital,wght@0,400;0,600;0,700;1,400&family=Oswald:wght@400;500;700&family=Roboto+Condensed:wght@700&display=swap" rel="stylesheet">
<style>
:root{
  --green:#4d9a12;
  --green-dark:#3f8010;
  --orange:#e8461b;
  --ink:#2e2e2e;
  --bar:#484848;
  --page:#f3f3f3;
  --line:#dcdcdc;
  --footer:#222222;
  --muted:#8a8a8a;
}
*{box-sizing:border-box;margin:0;padding:0}
html,body{width:810px;height:1200px;overflow:hidden}
body{position:relative;background:var(--page);font-family:"Open Sans",Arial,sans-serif;color:var(--ink)}

.hero{position:absolute;left:0;top:0;width:810px;height:442px;
  background:linear-gradient(100deg,#c9a9a2 0%,#b58aa4 25%,#d7b4bd 45%,#7a5c86 65%,#c7b4c4 85%,#9a8aa8 100%)}
.hero-photo{position:absolute;inset:0;
  background:radial-gradient(ellipse at 28% 45%,rgba(225,170,175,.7),transparent 55%),
             radial-gradient(ellipse at 72% 35%,rgba(70,50,90,.55),transparent 50%),
             linear-gradient(180deg,rgba(120,90,140,.25),rgba(230,190,200,.35))}

.topbar{position:absolute;left:0;top:0;width:810px;height:36px;background:rgba(40,40,45,.72)}
.brand{position:absolute;left:67px;top:0;width:106px;height:36px;background:var(--green);
  display:flex;align-items:center;justify-content:center;gap:6px;color:#fff;font-weight:700;font-size:17px}
.brand-dot{width:14px;height:14px;border-radius:50%;background:#fff}
.nav a{position:absolute;top:11px;color:#fff;font-size:11px;text-decoration:none}
.account{position:absolute;top:0;height:36px;display:flex;align-items:center;font-size:9px;color:#fff}
.signin{left:562px}
.or{left:599px;color:#aaa}
.signup{position:absolute;left:620px;top:10px;width:52px;height:17px;background:var(--green);border-radius:2px;
  color:#fff;font-size:9px;display:flex;align-items:center;justify-content:center}
.upload{left:691px}
.gear{position:absolute;left:735px;top:12px}

.search{position:absolute;left:170px;top:206px;width:473px;height:47px;background:rgba(50,50,50,.85);padding:5px}
.search-field{width:421px;height:37px;background:#f1f1f1;color:#b5b5b5;font-size:13px;padding:10px 13px}
.search-btn{position:absolute;right:5px;top:5px;width:39px;height:37px;background:var(--green);display:flex;align-items:center;justify-content:center}

.tagline{position:absolute;left:0;width:810px;text-align:center;font-family:"Oswald",sans-serif;font-weight:700;font-size:29px;letter-spacing:.5px}
.tagline.one{top:309px;color:var(--orange)}
.tagline.two{top:345px;color:var(--ink)}

.player{position:absolute;left:67px;top:450px;width:679px;height:95px}
.track-title{position:absolute;left:0;top:8px;color:var(--green);font-family:"Oswald",sans-serif;font-weight:500;font-size:14px}
.track-artist{position:absolute;left:0;top:28px;font-size:8px;font-style:italic;color:var(--muted)}
.track-stars{position:absolute;left:0;top:44px;color:var(--orange);font-size:11px;letter-spacing:1px}
.wave{position:absolute;left:73px;top:0}
.controls{position:absolute;left:0;top:70px;width:679px;height:22px;background:var(--bar)}
.ctrl-icons{position:absolute;left:11px;top:6px}
.progress{position:absolute;left:50px;top:8px;width:566px;height:6px;background:#fff;border-radius:3px;overflow:hidden}
.progress span{display:block;width:360px;height:6px;background:var(--green)}
.time{position:absolute;right:11px;top:5px;font-size:8px;font-style:italic;color:#fff}

.songs{position:absolute;left:67px;top:562px;width:679px;border-collapse:collapse;font-size:8px;table-layout:fixed}
.songs th{height:22px;background:var(--bar);color:var(--green);font-weight:600;font-size:8px}
.songs td{height:24px;border-bottom:1px solid var(--line);text-align:center;color:#444}
.songs th+th,.songs td+td{border-left:1px solid var(--line)}
.songs th:first-child,.songs td:first-child{text-align:left;padding-left:13px}
.songs .rate{color:var(--green);font-size:10px;letter-spacing:1px}
.buy{display:inline-block;background:var(--orange);color:#fff;padding:2px 6px;border-radius:2px;font-size:7.5px}

.events{position:absolute;left:67px;top:752px;width:679px;height:309px;
  background:radial-gradient(ellipse at 55% 50%,#9a6c84 0%,#b58397 35%,#c898ad 70%,#a97b93 100%)}
.events-title{position:absolute;left:163px;top:98px;width:353px;height:45px;background:var(--orange);
  color:#fff;font-family:"Roboto Condensed",sans-serif;font-weight:700;font-size:38px;text-align:center;line-height:45px}
.countdown{position:absolute;top:154px;width:82px;height:82px;border-radius:50%;color:#fff;text-align:center;font-family:"Oswald",sans-serif}
.countdown.dark{background:#111}
.countdown.lit{background:var(--green)}
.countdown b{display:block;font-size:38px;font-weight:500;line-height:1;padding-top:9px}
.countdown small{display:block;font-size:11px;margin-top:2px}

.footer{position:absolute;left:0;top:1072px;width:810px;height:128px;background:var(--footer);text-align:center}
.connect{position:absolute;left:0;top:14px;width:810px;font-family:"Oswald",sans-serif;font-size:17px;color:var(--orange)}
.connect em{font-style:normal;color:var(--green)}
.social{position:absolute;left:265px;top:50px;display:flex;gap:19px}
.social span{width:10px;height:10px;border-radius:50%;background:#fff}
.links{position:absolute;left:0;top:72px;width:810px;display:flex;justify-content:center;gap:24px;font-size:8px;color:#cfcfcf;letter-spacing:.5px}
.copyright{position:absolute;left:0;top:93px;width:810px;font-size:8px;color:#fff}
</style>
</head>
<body>

<header class="hero">
  <div class="hero-photo" role="img" aria-label="Photo of two friends on a beach, one playing an acoustic guitar"></div>
  <div class="topbar">
    <div class="brand"><span class="brand-dot"></span>Quarry</div>
    <nav class="nav"><a href="#" style="left:189px">Home</a><a href="#" style="left:236px">Explorer</a></nav>
    <span class="account signin">SIGN IN</span>
    <span class="account or">or</span>
    <span class="signup">SIGN UP</span>
    <span class="account upload">UPLOAD</span>
    <svg class="gear" width="12" height="12" viewBox="0 0 12 12"><circle cx="6" cy="6" r="4" fill="none" stroke="#fff" stroke-width="2.4" stroke-dasharray="2 1.2"/><circle cx="6" cy="6" r="2.4" fill="#fff"/><circle cx="6" cy="6" r="1.2" fill="#444"/></svg>
  </div>
  <div class="search">
    <div class="search-field">Type Your Keywords...</div>
    <div class="search-btn"><svg width="15" height="15" viewBox="0 0 15 15"><circle cx="6" cy="6" r="4.3" fill="none" stroke="#fff" stroke-width="2"/><path d="M9.2 9.2 13.5 13.5" stroke="#fff" stroke-width="2.4" stroke-linecap="round"/></svg></div>
  </div>
  <h1 class="tagline one">Share Your Songs With Quarry</h1>
  <p class="tagline two">and then enjoy...</p>
</header>

<section class="player">
  <h2 class="track-title">Open Roads</h2>
  <p class="track-artist">Dan Lorey</p>
  <p class="track-stars">★★★★★</p>
  <svg class="wave" width="606" height="67" viewBox="0 0 606 67">
    <path stroke="#4d9a12" stroke-width="2" d="M2 33V33M8 30V36M14 26V40M20 20V46M26 3V63M32 18V48M38 22V44M44 14V52M50 24V42M56 16V50M62 21V45M68 19V47M74 25V41M80 22V44M86 12V54M92 20V46M98 6V60M104 24V42M110 18V48M116 23V43M122 26V40M128 20V46M134 25V41M140 22V44M146 27V39M152 24V42M158 20V46M164 25V41M170 23V43M176 14V52M182 24V42M188 21V45M194 26V40M200 22V44M206 19V47M212 25V41M218 23V43M224 27V39M230 21V45M236 24V42M242 17V49M248 25V41M254 22V44M260 26V40M266 23V43M272 28V38M278 25V41M284 29V37M290 27V39M296 30V36M302 28V38M308 31V35M314 30V36M320 31V35M326 29V37M332 32V34M338 30V36M344 32V34"/>
    <path stroke="#9a9a9a" stroke-width="2" d="M352 24V42M358 8V58M364 20V46M370 26V40M376 14V52M382 22V44M388 25V41M394 18V48M400 24V42M406 10V56M412 22V44M418 26V40M424 19V47M430 24V42M436 12V54M442 23V43M448 26V40M454 20V46M460 24V42M466 27V39M472 16V50M478 22V44M484 25V41M490 19V47M496 24V42M502 21V45M508 26V40M514 18V48M520 23V43M526 9V57M532 20V46M538 4V62M544 22V44M550 28V38M556 31V35M562 32V34"/>
  </svg>
  <div class="controls">
    <svg class="ctrl-icons" width="28" height="10" viewBox="0 0 28 10"><path d="M5 1 1 5 5 9ZM9 1 5 5 9 9Z" fill="#4d9a12"/><rect x="12" y="1" width="2.5" height="8" fill="#fff"/><rect x="15.5" y="1" width="2.5" height="8" fill="#fff"/><path d="M21 1 25 5 21 9ZM24 1 28 5 24 9Z" fill="#4d9a12"/></svg>
    <div class="progress"><span></span></div>
    <span class="time">00.00 | 00.00</span>
  </div>
</section>

<table class="songs">
  <colgroup><col style="width:201px"><col style="width:102px"><col style="width:200px"><col style="width:99px"><col style="width:77px"></colgroup>
  <thead><tr><th>SONGS</th><th>Time Duration</th><th>Artist</th><th>Rating</th><th>Price</th></tr></thead>
  <tbody>
    <tr><td>Missing You</td><td>0:38</td><td>Artist 01</td><td class="rate">★★★★★</td><td><span class="buy">$20 Buy</span></td></tr>
    <tr><td>Midnight In Tokyo</td><td>2:51</td><td>Artist 02</td><td class="rate">★★★★★</td><td><span class="buy">$10 Buy</span></td></tr>
    <tr><td>Walking On Horizon</td><td>4:29</td><td>Artist 03</td><td class="rate">★★★★★</td><td><span class="buy">$60 Buy</span></td></tr>
    <tr><td>A Happy Carefree Day</td><td>2:45</td><td>Artist 04</td><td class="rate">★★★★★</td><td><span class="buy">$30 Buy</span></td></tr>
    <tr><td>Through the Clouds</td><td>5:56</td><td>Artist 05</td><td class="rate">★★★★★</td><td><span class="buy">$20 Buy</span></td></tr>
    <tr><td>Live My Life</td><td>3:56</td><td>Artist 06</td><td class="rate">★★★★★</td><td><span class="buy">$10 Buy</span></td></tr>
  </tbody>
</table>

<section class="events" role="img" aria-label="Photo of a young woman holding an acoustic guitar against a textured wall">
  <h2 class="events-title">UPCOMING EVENTS</h2>
  <div class="countdown dark" style="left:165px"><b>03</b><small>DAYS</small></div>
  <div class="countdown lit" style="left:254px"><b>23</b><small>HOURS</small></div>
  <div class="countdown dark" style="left:343px"><b>59</b><small>MINUTES</small></div>
  <div class="countdown lit" style="left:432px"><b>26</b><small>SECS</small></div>
</section>

<footer class="footer">
  <h2 class="connect">Connect <em>With Quarry</em></h2>
  <div class="social" aria-label="Social links"><span></span><span></span><span></span><span></span><span></span><span></span><span></span><span></span><span></span><span></span></div>
  <nav class="links"><span>HOME</span><span>EVENTS</span><span>ALBUMS</span><span>GALLERY</span><span>BLOG</span><span>FEATURES</span><span>SHOP</span></nav>
  <p class="copyright">Copyright © 2014 Quarry All rights reserved.</p>
</footer>

</body>
</html>
```